Quorvia medical teaching of the future

responsive website, onepager, for medical technology company. It has to look clean and high tech.

Look & feel
• Responsive
• Clean
• Combination icons + foto's
• Integration of a YouTube video

Landingpage items

• Header: picture + 'a video-based teaching platform for surgical procedures'
• About Deferred live medical teaching: Short description
• Features
o Video
o Teaching platform

• Benefits:
o More effective learning
o Faster sharing of knowledge & tecniques
o More cost effective

• References

• Products:
o Live (+link to more info)
o bTamo (+ link to more info)
o bTamo local (+link to more info)
o bTamo cloud (+ link to more info)

• Solutions:
o For medical device companies (+link to more info)
o Doctor and surgeons (+link to more info)
o Medical conferences (+link to more info)

Target Market(s)

medical device companies
surgeons and doctors
conference organisers

Industry/Entity Type

It Company

Number of Pages Required

1 page

Requirements
Must have
• Landingpage items
• • Header: picture + 'a video-based teaching platform for surgical procedures'
• • About Deferred live medical teaching: Short description
• • Features
• o Video
• o Teaching platform
• • Benefits:
• o More effective learning
• o Faster sharing of knowledge & tecniques
• o More cost effective
• • References
• • Products:
• o Live (+link to more info)
• o bTamo (+ link to more info)
• o bTamo local (+link to more info)
• o bTamo cloud (+ link to more info)
• • Solutions:
• o For medical device companies (+link to more info)
• o Doctor and surgeons (+link to more info)
• o Medical conferences (+link to more info)
Nice to have
• possibilty to show video

```html
<!DOCTYPE html>
<html lang="en">
<head>
<meta charset="utf-8">
<title>Quorvia – medical teaching of the future</title>
<link href="https://fonts.googleapis.com/css2?family=Open+Sans:wght@400;600;700&family=Oswald:wght@500&display=swap" rel="stylesheet">
<style>
:root{
  --red:#e8222d;
  --teal:#1f9d8b;
  --teal-dark:#16806f;
  --ink:#2d2d2d;
  --muted:#6b6b6b;
  --light:#f1f1f1;
  --line:#dedede;
  --white:#fff;
}
*{box-sizing:border-box;margin:0;padding:0}
html,body{width:1200px;height:3748px;overflow:hidden}
body{font-family:"Open Sans",Arial,sans-serif;color:var(--ink);background:var(--white);position:relative}
.abs{position:absolute}
h2{font-family:"Oswald","Open Sans",sans-serif;font-weight:500;font-size:30px;letter-spacing:.3px}
.brand{display:flex;align-items:center;gap:12px;font-weight:700;font-size:38px;color:var(--teal);white-space:nowrap}
.brand i{width:34px;height:34px;border-radius:50%;background:var(--red);display:block}

/* header */
.site-header{left:0;top:0;width:1200px;height:112px;background:var(--white)}
.site-header .brand{position:absolute;left:70px;top:30px}
.account{position:absolute;right:80px;top:14px;display:flex;gap:14px}
.account a{font-size:13px;font-weight:700;color:var(--white);padding:7px 16px;text-decoration:none}
.account .signup{background:var(--teal)}
.account .signin{background:var(--red)}
.main-nav{position:absolute;right:80px;top:68px;display:flex;gap:26px}
.main-nav a{font-size:15px;font-weight:600;color:var(--ink);text-decoration:none}
.main-nav a.active{color:var(--teal);border-bottom:2px solid var(--teal);padding-bottom:4px}

.media{background:linear-gradient(135deg,#8fb8c2,#4e7a86 45%,#2f4b55);}
.play{position:absolute;width:64px;height:64px;border-radius:50%;background:var(--red);display:flex;align-items:center;justify-content:center}
.play::after{content:"";border-left:20px solid var(--white);border-top:12px solid transparent;border-bottom:12px solid transparent;margin-left:6px}

.hero{left:0;top:112px;width:1200px;height:600px}

/* about */
.about{left:108px;top:660px;width:984px;height:372px;background:var(--white);box-shadow:0 4px 18px rgba(0,0,0,.12);text-align:center;padding:44px 120px 0}
.about h2{color:var(--ink);margin-bottom:22px}
.about p{font-size:15px;line-height:1.65;color:var(--muted);margin-bottom:20px}
.btn-red{display:inline-block;background:var(--red);color:var(--white);font-size:13px;font-weight:600;padding:10px 26px;text-decoration:none;margin-top:6px}

/* teaching platform */
.platform-band{left:0;top:1080px;width:480px;height:460px;background:var(--red)}
.platform-text{left:70px;top:1170px;width:340px;color:var(--white)}
.platform-text h2{font-size:30px;margin-bottom:18px}
.platform-text p{font-size:15px;line-height:1.6;margin-bottom:18px}
.platform-media{left:432px;top:1150px;width:768px;height:450px}

/* benefits */
.benefits{left:0;top:1640px;width:1200px;height:580px;background:var(--teal);color:var(--white);text-align:center}
.benefits h2{margin-top:42px}
.benefits .lead{width:780px;margin:22px auto 0;font-size:15px;line-height:1.6}
.benefit-row{position:absolute;left:140px;top:230px;width:920px;display:flex;justify-content:space-between}
.benefit{width:260px}
.benefit .icon{width:84px;height:84px;border-radius:50%;background:var(--white);margin:0 auto 22px;display:flex;align-items:center;justify-content:center}
.benefit h3{font-size:17px;font-weight:600;margin-bottom:10px}
.benefit p{font-size:13px;line-height:1.5;opacity:.9}

/* products */
.products{left:0;top:2240px;width:1200px;height:660px;background:var(--light);text-align:center}
.products h2{margin-top:60px}
.section-lead{width:600px;margin:16px auto 0;font-size:15px;line-height:1.6;color:var(--muted)}
.product-grid{position:absolute;left:80px;top:200px;width:1040px;display:flex;gap:8px}
.product{flex:1;background:var(--white);text-align:left}
.product .media{height:196px}
.product .body{padding:18px 18px 22px}
.product h3{font-size:17px;font-weight:700;margin-bottom:10px}
.product p{font-size:13px;line-height:1.5;color:var(--muted);margin-bottom:12px}
.more{font-size:13px;font-weight:600;color:var(--red);text-decoration:none}

/* solutions */
.solutions{left:0;top:2900px;width:1200px;height:470px;text-align:center}
.solutions h2{margin-top:50px}
.solution-grid{position:absolute;left:80px;top:190px;width:1040px;display:flex;justify-content:space-between}
.solution{width:320px;height:240px;display:flex;position:relative}
.solution .media{flex:1}
.solution .label{flex:1;background:var(--red);color:var(--white);display:flex;flex-direction:column;align-items:center;justify-content:center;gap:16px;font-size:17px;font-weight:600;padding:0 14px}
.solution .label.overlay{position:absolute;left:60px;right:60px;top:110px;bottom:20px;background:none}
.plus{width:30px;height:30px;border:2px solid var(--white);border-radius:50%;display:flex;align-items:center;justify-content:center;font-size:20px;line-height:1}

/* footer */
.site-footer{left:0;top:3370px;width:1200px;height:378px;background:var(--light)}
.site-footer .brand{position:absolute;left:70px;top:50px;font-size:30px}
.site-footer .brand i{width:26px;height:26px}
.footer-nav{position:absolute;left:300px;top:64px;display:flex;gap:26px}
.footer-nav a{font-size:14px;color:var(--ink);text-decoration:none}
.social{position:absolute;right:70px;top:52px;display:flex;gap:10px}
.social span{width:36px;height:36px;border:2px solid #9a9a9a;border-radius:50%;display:block}
.footer-cols{position:absolute;left:70px;top:130px;width:1060px;display:flex;justify-content:space-between}
.footer-col{width:230px}
.footer-col h4{font-size:15px;font-weight:700;margin-bottom:14px}
.footer-col p,.footer-col li{font-size:13px;line-height:1.7;color:var(--muted);list-style:none}
.field{font-size:12px;color:var(--muted);border-bottom:1px solid #bdbdbd;padding:6px 0;margin-bottom:10px}
.btn-submit{display:inline-block;border:1px solid #9a9a9a;font-size:12px;padding:6px 14px;margin-top:6px;color:var(--ink)}
.footer-bottom{position:absolute;left:70px;right:70px;top:325px;border-top:1px solid var(--line);padding-top:14px;display:flex;justify-content:space-between;font-size:12px;color:var(--muted)}
</style>
</head>
<body>

<header class="site-header abs">
  <div class="brand"><i></i>Quorvia</div>
  <div class="account"><a class="signup" href="#">SIGN UP</a><a class="signin" href="#">SIGN IN</a></div>
  <nav class="main-nav">
    <a class="active" href="#">HOME</a><a href="#">ABOUT</a><a href="#">FEATURES</a><a href="#">BENEFITS</a><a href="#">PRODUCTS</a><a href="#">SOLUTIONS</a><a href="#">CONTACT</a>
  </nav>
</header>

<section class="hero abs media" role="img" aria-label="Surgical team in an operating room, video player">
  <span class="play" style="left:568px;top:220px"></span>
</section>

<section class="about abs">
  <h2>About Deferred Live Medical Teaching</h2>
  <p>Quorvia is building a video based teaching platform for all kinds of medical procedures using synchronised high resolution 360° and wide angle video in a virtual reality environment. Quorvia changes the way medical procedures are taught.</p>
  <p>Almost daily medical device companies, doctors and surgeons all over the world develop new or breakthrough products, medical and surgical techniques. These techniques save lives or increase the survival rate of some patients.</p>
  <a class="btn-red" href="#">Explore More</a>
</section>

<div class="platform-band abs"></div>
<section class="platform-text abs">
  <h2>The Teaching Platform</h2>
  <p>Once the surgery is captured all the info can be streamed online with the unique feature that, although the surgery is filmed in advance, the presenter has real time full control over the imaging he wants to see.</p>
  <p>Better than in a live surgery! The presenter of the live session can experience each step of the surgery completely in his own way by navigating through the corresponding omnidirectional imaging.</p>
</section>
<div class="platform-media abs media" role="img" aria-label="Surgeons operating with monitors, video player">
  <span class="play" style="left:352px;top:193px"></span>
</div>

<section class="benefits abs">
  <h2>Benefits</h2>
  <p class="lead">Medical and surgical knowledge can be shared in a faster, easier and more cost effective way than current solutions like movies and pre-edited video.</p>
  <div class="benefit-row">
    <div class="benefit">
      <div class="icon"><svg width="40" height="40" viewBox="0 0 40 40" fill="none" stroke="#1f9d8b" stroke-width="2.5"><circle cx="11" cy="20" r="5"/><circle cx="29" cy="10" r="5"/><circle cx="29" cy="30" r="5"/><path d="M15 18l10-6M15 22l10 6"/></svg></div>
      <h3>Faster Sharing</h3>
      <p>Faster sharing of knowledge and new techniques to surgeons worldwide due to the cloud based learning platform</p>
    </div>
    <div class="benefit">
      <div class="icon"><svg width="40" height="40" viewBox="0 0 40 40" fill="none" stroke="#1f9d8b" stroke-width="2.5"><path d="M4 15l16-8 16 8-16 8z"/><path d="M10 18v9c6 5 14 5 20 0v-9"/></svg></div>
      <h3>Easier Learning</h3>
      <p>Easier learning due to advanced video based interactivity and state of the art medical illustrations clarifying each step</p>
    </div>
    <div class="benefit">
      <div class="icon"><svg width="40" height="40" viewBox="0 0 40 40" fill="none" stroke="#1f9d8b" stroke-width="2.5"><circle cx="20" cy="20" r="14"/><path d="M24 14h-6a3 3 0 000 6h4a3 3 0 010 6h-6M20 10v4M20 26v4"/></svg></div>
      <h3>More Cost-Effective</h3>
      <p>More cost effective compared to traditional teaching methods</p>
    </div>
  </div>
</section>

<section class="products abs">
  <h2>Products</h2>
  <p class="section-lead">It is a long established fact that a reader will be distracted by the readable content of a page more on less normal distribution of letters when looking at its layout.</p>
  <div class="product-grid">
    <article class="product"><div class="media" role="img" aria-label="Operating room with surgical lights"></div><div class="body"><h3>Live</h3><p>It is a long established fact that a reader will be distracted more on normal distribution of letters.</p><a class="more" href="#">» More info</a></div></article>
    <article class="product"><div class="media" role="img" aria-label="Surgeons at work"></div><div class="body"><h3>bTamo</h3><p>It is a long established fact that a reader will be distracted more on normal distribution of letters.</p><a class="more" href="#">» More info</a></div></article>
    <article class="product"><div class="media" role="img" aria-label="Surgical team at the table"></div><div class="body"><h3>bTamo local</h3><p>It is a long established fact that a reader will be distracted more on normal distribution of letters.</p><a class="more" href="#">» More info</a></div></article>
    <article class="product"><div class="media" role="img" aria-label="Surgeons with screens"></div><div class="body"><h3>bTamo cloud</h3><p>It is a long established fact that a reader will be distracted more on normal distribution of letters.</p><a class="more" href="#">» More info</a></div></article>
  </div>
</section>

<section class="solutions abs">
  <h2>Solutions</h2>
  <p class="section-lead">It is a long established fact that a reader will be distracted by the readable content of a page more on less normal distribution of letters when looking at its layout.</p>
  <div class="solution-grid">
    <div class="solution"><div class="media" role="img" aria-label="Medical device in use"></div><div class="label">For Medical Device Companies<span class="plus">+</span></div></div>
    <div class="solution"><div class="media" role="img" aria-label="Doctors and surgeons operating"></div><div class="label overlay">Doctor and Surgeons<span class="plus">+</span></div></div>
    <div class="solution"><div class="media" role="img" aria-label="Conference audience watching a screen"></div><div class="label">Medical Conferences<span class="plus">+</span></div></div>
  </div>
</section>

<footer class="site-footer abs">
  <div class="brand"><i></i>Quorvia</div>
  <nav class="footer-nav"><a href="#">Home</a><a href="#">About</a><a href="#">Features</a><a href="#">Benefits</a><a href="#">Products</a><a href="#">Solutions</a><a href="#">Contact</a></nav>
  <div class="social"><span></span><span></span><span></span><span></span><span></span></div>
  <div class="footer-cols">
    <div class="footer-col"><h4>Newsletter Sign Up</h4><div class="field">Name</div><div class="field">Email</div><span class="btn-submit">SUBMIT</span></div>
    <div class="footer-col"><h4>Contact Us</h4><p>Quorvia deferred live medical teaching<br>14 Halden Row, Brickfield Lane<br>Northmere 40210</p><p>T: 0612 448 302<br>E: hello@quorvia.example</p></div>
    <div class="footer-col"><h4>Our Products</h4><ul><li>Live</li><li>bTamo</li><li>bTamo Local</li><li>bTamo Cloud</li></ul></div>
    <div class="footer-col"><h4>Solutions</h4><ul><li>For medical device companies</li><li>Doctors and surgeons</li><li>Medical conferences</li></ul></div>
  </div>
  <div class="footer-bottom"><span>Copyright 2017 All Rights Reserved</span><span>Terms of Use &nbsp; Privacy Policy</span></div>
</footer>

</body>
</html>
```